MD Business Card

I want to create a simple business card.
I am a consultant. I design and develop furniture, lighting and accessories for hospitality and retail brands.
I want the card to be simple and clean. Not too much of a logo - but it needs the basic information shown on the attached file.
Also - I have shown some fonts that I like on the attached file.
The card can be square or rectangle. It should be double sided.
I prefer 1-2 colors (not too colorful - but using color an an accent) Even if using color on the edges as an accent.

My snapquilt link shows some other graphics styles that I like. I like clean and simple.
http://www.snapquilt.com/marendowsett/business-cards/

Reason: I needed a few more days to see some of the options evolve.

Hospitality

```html
<!DOCTYPE html>
<html lang="en">
<head>
<meta charset="utf-8">
<title>Maren Dowsett — Business Card</title>
<link rel="stylesheet" href="https://fonts.googleapis.com/css2?family=Oswald:wght@300;700&display=swap">
<style>
  :root {
    --brown: #654036;
    --magenta: #c81e64;
    --paper: #fbfbfa;
    --backdrop: #e4e4e2;
    --ink-light: #ffffff;
  }
  * { box-sizing: border-box; margin: 0; padding: 0; }
  html, body {
    width: 1200px;
    height: 1000px;
    overflow: hidden;
    background: var(--backdrop);
    font-family: "Oswald", sans-serif;
  }
  .card {
    position: absolute;
    left: 250px;
    width: 700px;
    height: 400px;
    background: var(--paper);
    box-shadow: 0 6px 18px rgba(0,0,0,0.18);
    overflow: hidden;
  }
  .card--back { top: 70px; display: flex; align-items: center; justify-content: center; }
  .card--front { top: 530px; }

  .back-name {
    color: var(--brown);
    font-weight: 700;
    font-size: 78px;
    letter-spacing: 2px;
    text-transform: uppercase;
  }

  .front-shapes { position: absolute; inset: 0; width: 700px; height: 400px; }

  .front-name {
    position: absolute;
    left: 30px;
    top: 108px;
    width: 230px;
    text-align: center;
    color: var(--brown);
    font-weight: 700;
    font-size: 62px;
    line-height: 1.22;
    letter-spacing: 1px;
    text-transform: uppercase;
  }

  .front-info {
    position: absolute;
    left: 350px;
    top: 42px;
    width: 330px;
    text-align: center;
    color: var(--ink-light);
    font-weight: 300;
  }
  .tagline { font-size: 31px; letter-spacing: 0.5px; line-height: 1.2; }
  .tagline u { text-decoration-thickness: 1px; text-underline-offset: 4px; }
  .services { margin-top: 10px; font-size: 23px; line-height: 1.2; }
  .contact { position: absolute; left: 350px; top: 268px; width: 340px; text-align: center; color: var(--ink-light); font-weight: 300; }
  .email { font-size: 25px; letter-spacing: 0.3px; }
  .phone { margin-top: 8px; font-size: 30px; }
</style>
</head>
<body>
  <section class="card card--back">
    <h1 class="back-name">Maren Dowsett</h1>
  </section>

  <section class="card card--front">
    <svg class="front-shapes" viewBox="0 0 700 400" aria-hidden="true">
      <path fill="var(--magenta)" d="M262 0 C318 100 300 280 150 400 L700 400 L700 0 Z"/>
      <path fill="var(--paper)" d="M268 0 C326 100 318 280 185 400 L700 400 L700 0 Z"/>
      <path fill="var(--brown)" d="M276 0 C334 100 330 280 205 400 L700 400 L700 0 Z"/>
    </svg>

    <h2 class="front-name">Maren<br>Dowsett</h2>

    <div class="front-info">
      <p class="tagline">HOSPITALITY <u>&amp;</u> HOME</p>
      <p class="services">FF&amp;E, furniture, lighting,<br>textiles, etc.</p>
    </div>

    <div class="contact">
      <p class="email">maren@marendowsett.com</p>
      <p class="phone">917.555.0148</p>
    </div>
  </section>
</body>
</html>
```